Building Company Business Card Design

I am looking to get a business card designed for my Building Company. Please find the logo attached.

Industry/Entity Type

Business

Contact Information for Business Card

Mobile 0472 913 046
Email admin@tarrowconstructworks.com.au
Website www.tarrowconstructworks.com.au

Colors
0255a3

```html
<!DOCTYPE html>
<html lang="en">
<head>
<meta charset="utf-8">
<title>Tarrow Construct Works – Business Card</title>
<link href="https://fonts.googleapis.com/css2?family=Open+Sans:wght@400;600;700&display=swap" rel="stylesheet">
<style>
  :root {
    --brand-blue: #0255a3;
    --swoosh-grey: #7d7f83;
    --ink: #4a4c50;
    --rule: #9a9ca0;
    --paper: #f4f4f4;
    --paper-edge: #e4e4e4;
    --back-dark: #55585c;
    --back-light: #76797d;
    --stage: #2d2f33;
    --white: #ffffff;
  }
  * { margin: 0; padding: 0; box-sizing: border-box; }
  html, body { width: 1200px; height: 960px; overflow: hidden; }
  body {
    background: var(--stage);
    font-family: "Open Sans", Arial, sans-serif;
    position: relative;
  }
  .card {
    position: absolute;
    left: 215px;
    width: 770px;
    height: 440px;
    overflow: hidden;
    box-shadow: 0 10px 30px rgba(0,0,0,.45);
  }
  .card--front { top: 25px; background: linear-gradient(135deg, var(--white), var(--paper) 60%, var(--paper-edge)); }
  .card--back { top: 495px; background: linear-gradient(160deg, var(--back-light), var(--back-dark)); }

  .front-band { position: absolute; inset: 0; width: 100%; height: 100%; }

  .holder { position: absolute; left: 36px; top: 30px; color: var(--white); }
  .holder__name { font-weight: 700; font-size: 20px; letter-spacing: .3px; }
  .holder__role { font-weight: 400; font-size: 15px; margin-top: 2px; }

  .company-name {
    position: absolute;
    right: 40px;
    top: 168px;
    text-align: right;
    color: var(--brand-blue);
    font-weight: 700;
    font-size: 34px;
    line-height: 1.08;
    letter-spacing: 1px;
  }

  .rule { position: absolute; height: 1px; background: var(--rule); }
  .rule--top { left: 36px; right: 290px; top: 252px; }
  .rule--bottom { left: 300px; right: 36px; top: 362px; }

  .contacts { position: absolute; left: 36px; top: 268px; list-style: none; }
  .contacts li {
    display: flex; align-items: center; gap: 10px;
    font-size: 16px; color: var(--ink); line-height: 25px;
  }
  .contacts svg { width: 13px; height: 13px; fill: var(--brand-blue); flex: none; }

  .address {
    position: absolute; right: 36px; top: 372px;
    text-align: right; color: var(--ink); font-size: 17px; line-height: 23px;
  }

  .back-name {
    position: absolute; left: 0; right: 0; top: 150px;
    text-align: center; color: var(--white);
    font-weight: 700; font-size: 46px; letter-spacing: 3px;
  }
  .back-site {
    position: absolute; left: 0; right: 0; top: 300px;
    text-align: center; color: #e6e6e6;
    font-size: 17px; letter-spacing: 3px;
  }
</style>
</head>
<body>

  <section class="card card--front">
    <svg class="front-band" viewBox="0 0 770 440" preserveAspectRatio="none" aria-hidden="true">
      <path d="M0 0 H770 V150 C560 95 260 90 0 140 Z" fill="var(--brand-blue)"/>
      <path d="M0 140 C260 90 560 95 770 150 V156 C560 108 280 104 0 172 Z" fill="var(--swoosh-grey)"/>
    </svg>

    <div class="holder">
      <div class="holder__name">LIAM HARGREAVE</div>
      <div class="holder__role">CEO/FOUNDER</div>
    </div>

    <div class="company-name">TARROW<br>CONSTRUCT WORKS</div>

    <div class="rule rule--top"></div>

    <ul class="contacts">
      <li>
        <svg viewBox="0 0 16 16"><path d="M3 1h3l1.5 4-2 1.3a9 9 0 0 0 4.2 4.2L11 8.5l4 1.5v3a2 2 0 0 1-2 2A13 13 0 0 1 1 3a2 2 0 0 1 2-2z"/></svg>
        <span>0472 913 046</span>
      </li>
      <li>
        <svg viewBox="0 0 16 16"><path d="M1 3h14v10H1z M1 3l7 6 7-6" stroke="#fff" stroke-width="1"/></svg>
        <span>admin@tarrowconstructworks.com.au</span>
      </li>
      <li>
        <svg viewBox="0 0 16 16"><circle cx="8" cy="8" r="7"/></svg>
        <span>www.tarrowconstructworks.com.au</span>
      </li>
    </ul>

    <div class="rule rule--bottom"></div>

    <address class="address" style="font-style:normal">
      4821 Ironbark Street<br>
      Bendigo, Victoria 35501
    </address>
  </section>

  <section class="card card--back">
    <div class="back-name">TARROW</div>
    <div class="back-site">tarrowconstructworks.com.au</div>
  </section>

</body>
</html>
```